Velvet Dare Age Verification Landing Page

To create a visually appealing design for the landing page of the adult game "Velvet Dare" that confirms the visitor's age.
The design should have a simple and visually appealing look that focuses on two buttons labeled "Yes" and "No". The purpose of the page is to confirm that the visitor is 18 years of age or older before accessing the game's content. Responsive design that works well on desktop and mobile devices. The final output should be delivered in PSD, AI, or Sketch format, along with any necessary images or assets.
I have also attached examples.

```html
<!DOCTYPE html>
<html lang="en">
<head>
<meta charset="utf-8">
<title>Velvet Dare — Age Verification</title>
<link rel="stylesheet" href="https://fonts.googleapis.com/css2?family=Inter:wght@400;600;700&family=Urbanist:wght@400;600;700&display=swap">
<style>
  :root{
    --page-bg:#0b0b0d;
    --page-text:#ffffff;
    --accent-violet:#3a2bd1;
    --accent-orange:#f59a1c;
    --veil:rgba(0,0,0,0.82);
    --card-bg:#1e1e1e;
    --frame-light:#e08ee6;
    --frame-dark:#a04fae;
    --pink-soft:#f8c8f8;
    --pink-label:#e8a6ec;
    --btn-primary-top:#e690ea;
    --btn-primary-bottom:#8e3f9c;
    --btn-dark-top:#3a3a3a;
    --btn-dark-bottom:#141414;
  }
  *{box-sizing:border-box;margin:0;padding:0}
  html,body{width:1200px;height:960px;overflow:hidden;background:var(--page-bg)}
  body{position:relative;font-family:"Urbanist",sans-serif;color:var(--page-text)}

  /* underlying game site */
  .site{position:absolute;inset:0}
  .site-nav{position:absolute;top:0;left:0;width:100%;height:68px}
  .site-brand{position:absolute;left:-2px;top:20px;font-size:21px;font-weight:600}
  .site-links{position:absolute;left:310px;top:25px;display:flex;gap:26px;font-size:15px}
  .site-btn{position:absolute;top:11px;height:33px;border-radius:8px;font-size:9px;font-weight:700;letter-spacing:1px;display:flex;align-items:center;justify-content:center}
  .site-btn--account{left:906px;width:76px;border:1.5px solid #fff}
  .site-btn--subscribe{left:991px;width:82px;background:var(--accent-orange)}
  .hero-title{position:absolute;left:-170px;top:210px;font-size:66px;font-weight:600;line-height:74px;white-space:nowrap}
  .hero-copy{position:absolute;left:-120px;top:374px;font-size:19px;line-height:27px;white-space:nowrap}
  .hero-cta{position:absolute;top:452px;height:42px;border-radius:10px;font-size:10px;font-weight:700;letter-spacing:1px;display:flex;align-items:center;justify-content:center}
  .hero-cta--buy{left:-60px;width:114px;background:var(--accent-violet)}
  .hero-cta--learn{left:67px;width:106px;border:1.5px solid #fff}
  .hero-art{position:absolute;left:700px;top:170px;width:450px;height:440px;border-radius:40px;background:radial-gradient(ellipse at 40% 45%,#b25aa8 0%,#6a2f7a 45%,#2a1638 75%,transparent 100%)}
  .update-title{position:absolute;left:24px;top:728px;font-size:40px;font-weight:600;line-height:43px}
  .update-copy{position:absolute;left:24px;top:823px;font-size:15px;line-height:21px}
  .update-cta{top:886px;height:42px}
  .update-cta.hero-cta--buy{left:24px;width:108px}
  .update-cta.hero-cta--learn{left:144px;width:107px}
  .class-icons{position:absolute;left:504px;top:790px;display:flex;gap:28px}
  .class-icon{width:100px;height:100px;border-radius:24px}
  .class-icon--arcane{background:radial-gradient(circle,#8a35c8,#2a1240)}
  .class-icon--nature{background:radial-gradient(circle,#1fb07a,#0c3325)}
  .class-icon--fire{background:radial-gradient(circle,#f59a1c,#4a2307)}
  .class-icon--frost{background:radial-gradient(circle,#2f7fe0,#0d2340)}
  .veil{position:absolute;inset:0;background:var(--veil)}

  /* age gate */
  .age-gate{position:absolute;left:466px;top:154px;width:268px;height:652px}
  .age-gate__frame{position:absolute;inset:0}
  .age-gate__content{position:absolute;inset:0;text-align:center;font-family:"Inter",sans-serif}
  .brand{position:absolute;left:0;right:0;top:90px;display:flex;flex-direction:column;align-items:center;gap:30px}
  .brand__dot{width:84px;height:84px;border-radius:50%;background:var(--pink-soft)}
  .brand__name{font-size:26px;font-weight:600;color:#fff}
  .age-gate__question{position:absolute;left:0;right:0;top:404px;font-size:13.5px;font-weight:600}
  .age-btn{position:absolute;left:37px;width:195px;height:45px;border-radius:23px;font-size:15px;font-weight:700;display:flex;align-items:center;justify-content:center;color:#fff}
  .age-btn--confirm{top:439px;background:linear-gradient(var(--btn-primary-top),var(--btn-primary-bottom))}
  .age-btn--exit{top:498px;background:linear-gradient(var(--btn-dark-top),var(--btn-dark-bottom))}
  .remember{position:absolute;left:0;right:0;top:564px;display:flex;align-items:center;justify-content:center;gap:9px;font-size:12px;letter-spacing:.4px;color:var(--pink-label)}
  .remember__box{width:12px;height:12px;background:var(--pink-label)}
</style>
</head>
<body>
  <div class="site" aria-hidden="true">
    <header class="site-nav">
      <div class="site-brand">Mythfall</div>
      <nav class="site-links"><span>Overview</span><span>Features</span><span>Getting Started</span><span>Meida</span><span>FAQ</span></nav>
      <div class="site-btn site-btn--account">ACCOUNT</div>
      <div class="site-btn site-btn--subscribe">SUBSCRIBE</div>
    </header>
    <h1 class="hero-title">A beautiful game,<br>intense reality</h1>
    <p class="hero-copy">Welcome to Mythfall, the strategy card game<br>that's easy to learn but impossible to put down!</p>
    <div class="hero-cta hero-cta--buy">BUY NOW</div>
    <div class="hero-cta hero-cta--learn">LEARN MORE</div>
    <div class="hero-art" role="img" aria-label="Illustration of the game's heroines"></div>
    <h2 class="update-title">Synergy of the light<br>update is now live</h2>
    <p class="update-copy">Combine new spells and character abilities however you<br>want. Create your own classes and share your decks.</p>
    <div class="hero-cta hero-cta--buy update-cta">BUY NOW</div>
    <div class="hero-cta hero-cta--learn update-cta">LEARN MORE</div>
    <div class="class-icons">
      <div class="class-icon class-icon--arcane" role="img" aria-label="Arcane class emblem"></div>
      <div class="class-icon class-icon--nature" role="img" aria-label="Nature class emblem"></div>
      <div class="class-icon class-icon--fire" role="img" aria-label="Fire class emblem"></div>
      <div class="class-icon class-icon--frost" role="img" aria-label="Frost class emblem"></div>
    </div>
    <div class="veil"></div>
  </div>

  <section class="age-gate" aria-labelledby="age-question">
    <svg class="age-gate__frame" width="268" height="652" viewBox="0 0 268 652">
      <defs>
        <linearGradient id="frameGrad" x1="0" y1="0" x2="0" y2="1">
          <stop offset="0" stop-color="var(--frame-light)"/>
          <stop offset="1" stop-color="var(--frame-dark)"/>
        </linearGradient>
      </defs>
      <path d="M54,60 L54,24 Q134,-16 214,24 L214,60 Q264,62 264,112 L264,540 Q264,590 214,592 L214,628 Q134,668 54,628 L54,592 Q4,590 4,540 L4,112 Q4,62 54,60 Z" fill="var(--card-bg)" stroke="url(#frameGrad)" stroke-width="8"/>
      <path d="M64,68 L64,33 Q134,-1 204,33 L204,68 Q254,70 254,118 L254,534 Q254,582 204,584 L204,619 Q134,653 64,619 L64,584 Q14,582 14,534 L14,118 Q14,70 64,68 Z" fill="none" stroke="url(#frameGrad)" stroke-width="2.5"/>
    </svg>
    <div class="age-gate__content">
      <div class="brand">
        <span class="brand__dot"></span>
        <span class="brand__name">Velvet Dare</span>
      </div>
      <p class="age-gate__question" id="age-question">Are you over 18 years of age?</p>
      <div class="age-btn age-btn--confirm">I’M OVER 18</div>
      <div class="age-btn age-btn--exit">EXIT</div>
      <label class="remember"><span class="remember__box"></span>Remember me</label>
    </div>
  </section>
</body>
</html>
```